Business cards design on a high standard

We advise clients on insurance and financial matters, since these clients pay for our advice, the design should have a high standard. Our logo should be included. From the colors we are open for everything.

Colors

Designer to choose colors to be used in the design.

```html
<!DOCTYPE html>
<html lang="en">
<head>
<meta charset="utf-8">
<title>Crestline Advisory – Business Cards</title>
<link href="https://fonts.googleapis.com/css2?family=Roboto:wght@300;400;700&display=swap" rel="stylesheet">
<style>
  :root {
    --bg: #2a2a2c;
    --card-dark: #333335;
    --logo-dark: #252527;
    --red: #e60000;
    --grey: #a7a8ab;
    --text-grey: #8e8f92;
    --white: #ffffff;
  }
  * { margin: 0; padding: 0; box-sizing: border-box; }
  html, body { width: 1200px; height: 880px; overflow: hidden; }
  body {
    background: var(--bg);
    font-family: "Roboto", Arial, sans-serif;
    position: relative;
  }
  .card {
    position: absolute;
    width: 520px;
    height: 300px;
    border-radius: 18px;
    overflow: hidden;
  }
  .card--back {
    left: 60px; top: 140px;
    background: var(--card-dark);
    display: flex; align-items: center; justify-content: center;
  }
  .card--back .brand-name {
    color: var(--logo-dark);
    font-size: 40px;
  }
  .card--front {
    left: 620px; top: 440px;
    background: var(--white);
  }
  .card-shape { position: absolute; inset: 0; }
  .brand-name {
    font-weight: 700;
    letter-spacing: 2px;
    text-transform: uppercase;
    line-height: 1;
  }
  .front-content { position: absolute; inset: 0; }
  .person {
    position: absolute; right: 40px; top: 26px; text-align: right;
  }
  .person-name { color: var(--red); font-weight: 700; font-size: 21px; }
  .person-title { color: var(--text-grey); font-weight: 300; font-size: 15px; margin-top: 2px; }
  .card--front .brand-name {
    position: absolute; left: 150px; top: 104px;
    color: var(--red); font-size: 32px;
  }
  .contact {
    position: absolute; left: 180px; top: 168px; width: 270px;
    list-style: none; color: var(--text-grey); font-size: 14px; font-weight: 300;
  }
  .contact li { display: flex; align-items: center; gap: 9px; height: 22px; }
  .contact svg { width: 11px; height: 11px; flex: none; }
  .contact .accent { color: var(--red); }
  .address {
    position: absolute; left: 180px; top: 246px; width: 270px;
    border-top: 1px solid var(--grey); padding-top: 7px;
    color: var(--text-grey); font-size: 14px; font-weight: 300;
  }
</style>
</head>
<body>

<section class="card card--back" aria-label="Card back">
  <span class="brand-name">Crestline Advisory</span>
</section>

<section class="card card--front" aria-label="Card front">
  <svg class="card-shape" viewBox="0 0 520 300" aria-hidden="true">
    <rect width="520" height="300" fill="var(--red)"/>
    <ellipse cx="300" cy="120" rx="268" ry="218" transform="rotate(-22 300 120)" fill="var(--grey)"/>
    <ellipse cx="298" cy="124" rx="258" ry="210" transform="rotate(-22 298 124)" fill="var(--white)"/>
    <ellipse cx="306" cy="118" rx="250" ry="206" transform="rotate(-22 306 118)" fill="var(--white)"/>
  </svg>
  <div class="front-content">
    <div class="person">
      <div class="person-name">Daniel Moreau</div>
      <div class="person-title">Manager</div>
    </div>
    <span class="brand-name">Crestline Advisory</span>
    <ul class="contact">
      <li>
        <svg viewBox="0 0 12 12"><path fill="var(--red)" d="M2.5 1l2 2.2-1 1.3a7 7 0 0 0 4 4l1.3-1 2.2 2-1.3 1.5C5 10.5 1.5 7 1 2.3z"/></svg>
        555-018-2746
      </li>
      <li>
        <svg viewBox="0 0 12 12"><rect x="0.5" y="2" width="11" height="8" fill="var(--red)"/><path d="M0.5 2.5 6 7l5.5-4.5" stroke="var(--white)" fill="none"/></svg>
        hello@crestlinemail.com
      </li>
      <li>
        <svg viewBox="0 0 12 12"><circle cx="6" cy="6" r="5.5" fill="var(--red)"/><circle cx="6" cy="6" r="2" fill="var(--white)"/></svg>
        <span>www.<span class="accent">crestlineadvisory</span>.com</span>
      </li>
    </ul>
    <div class="address">48 Harbor Lane, Lakeside, ZIP 4021</div>
  </div>
</section>

</body>
</html>
```